Home page design for Drone video business (the Business focusses on home videos for realtors)

Dear reader,

*I NEED DESIGNS OF ALL THE PAGES*
We need a first design of a homepage and of 4 other pages of the website of a business that sells drone video services. All the pages will need to be in the similar design style.
The video's are targeted at consumers that want to sell there home and would like to have a cool drone video of photos of their home.

How does the website look:
- has a navbar on top
- A cool looking banner of an areal drone.
- A Big header: with company name: SkyNestClips
- A smaller subheader: We film your home to increase your chances of sale
- Then a section with a Big header: How does it work
- In this section a place for a vimeo explainitory video
- Then a similar navbar styled bar with a phone number and a email address
- Then a section where the videos porfolio is displayed in a cool way
- Inside this sectiona header: Our work

- A section with header: Why us?
- 4 symbols here with a subheader and some lorum ipsum text underneath (see wireframe images)

- Under that a: Contact us
- where you can put in name, email, phone, message box and a send button

- At the bottom a footer with phone number and a fake address for now.

Be creative. Use creative but serious color.
Use a serious font. Make it a sharp design. Sharp lines. Not to dark design and not to light design.

The wireframes are the same kind of images.
PLEASE PUT IN DESIGNS OF ALL THE PAGES

Good luck

Target Market(s)

People that want to sell home and want to make a cool drone video or photos of their home.

Industry/Entity Type

Business

Contact Information for Business Card

Lucas Verbeek
lucas@skynestclips.example
+31647203519

Logo Text

SkyNestClips

Number of Pages Required

1 page

Font styles to use
Sans Serif

Requirements
Must have
• All the sections as explained in the instructions.
• The nav bar should have an about us, services, portfolio and a contact us buttons.
• See instruction for details.
• Must include designs of the front page, contact us, our services, portfolio and contact us.
• If you do add some designs for the "about us", "services", "prices", "portfolio" and "contact us" pages, you make a way better chance of winning the competition.
Nice to have
• designs for the other pages as described at the Must haves. You make a better chance of winning if you include them. Look at the wireframes to see the mockups for those pages. think creative about what kind of sections and design should be included in those pages.
Should not have
• bad designs.

```html
<!DOCTYPE html>
<html lang="en">
<head>
<meta charset="utf-8">
<title>SkyNestClips – Services</title>
<link href="https://fonts.googleapis.com/css2?family=Lato:wght@400;700&display=swap" rel="stylesheet">
<style>
:root{
  --teal:#0b6a6f;
  --teal-band:rgba(11,106,111,.88);
  --ink:#111;
  --body:#2a2a2a;
  --grey-band:#e6e6e6;
  --footer-line:rgba(255,255,255,.25);
  --bottom:#0c0c0c;
  --white:#fff;
}
*{box-sizing:border-box;margin:0;padding:0}
html,body{width:1200px;height:2253px;overflow:hidden}
body{font-family:"Lato",Arial,sans-serif;color:var(--body);background:var(--white);position:relative}
.wrap{width:1002px;margin:0 auto;position:relative}

/* header */
.site-header{height:118px;background:var(--white)}
.site-header .wrap{height:118px}
.brand{position:absolute;left:0;top:74px;display:flex;align-items:center;gap:10px}
.brand-mark{width:22px;height:22px;background:var(--teal)}
.brand-name{font-size:28px;font-weight:700;color:var(--ink);line-height:1}
.contact-line{position:absolute;right:0;top:14px;display:flex;gap:22px;align-items:center}
.contact-item{display:flex;align-items:center;gap:10px;font-size:19px;color:var(--ink)}
.contact-item.email{font-size:16px}
.icon-round{width:35px;height:35px;border-radius:50%;background:var(--teal);display:flex;align-items:center;justify-content:center}
.main-nav{position:absolute;right:0;top:80px;display:flex}
.main-nav a{display:block;font-size:14px;font-weight:700;color:var(--ink);text-decoration:none;padding:4px 21px 13px;position:relative}
.main-nav a:last-child{padding-right:0}
.main-nav a.home{color:var(--teal)}
.main-nav a.active::after{content:"";position:absolute;left:12px;right:12px;bottom:0;height:3px;background:var(--teal)}

/* hero */
.hero{height:335px;position:relative;background:linear-gradient(180deg,#6d8fb8 0%,#7b7066 28%,#8a6a55 50%,#4f6b3a 75%,#3f5e2c 100%)}
.hero-band{position:absolute;left:0;right:0;bottom:0;height:87px;background:var(--teal-band);text-align:center;color:var(--white)}
.hero-band h1{font-weight:400;font-size:38px;letter-spacing:.5px;margin-top:6px;line-height:1.15}
.hero-band p{font-size:22px;margin-top:2px}

/* breadcrumb */
.breadcrumb{height:39px;background:linear-gradient(#f6f6f6,#e8e8e8)}
.breadcrumb .wrap{display:flex;align-items:center;gap:8px;height:39px;padding-left:26px;font-size:12px;font-weight:700;color:var(--teal)}
.breadcrumb .sep{color:#777;font-weight:400}

/* services */
.page-title{text-align:center;color:var(--teal);font-size:33px;font-weight:700;padding-top:38px;height:94px}
.service{height:280px}
.service.alt{background:var(--grey-band)}
.service.first{height:238px}
.service .wrap{display:flex;gap:32px;height:100%;align-items:flex-start}
.service.alt .wrap{flex-direction:row-reverse;justify-content:space-between}
.service:not(.first) .wrap{padding-top:43px}
.service-photo{width:301px;height:194px;flex:none}
.service-body{flex:1}
.service.alt .service-body{flex:none;width:672px}
.service-body h2{font-size:19px;font-weight:700;color:var(--ink);margin-top:-2px;margin-bottom:6px}
.service-body p{font-size:13.3px;line-height:24px;color:var(--body)}
.read-more{display:inline-block;margin-top:15px;background:var(--teal);color:var(--white);font-size:13.5px;padding:6px 10px;text-decoration:none;box-shadow:0 5px 5px -4px rgba(0,0,0,.35)}

/* footer */
.site-footer{position:absolute;left:0;top:1944px;width:1200px;height:264px;background:var(--teal);color:var(--white)}
.site-footer .wrap{height:264px}
.f-col{position:absolute;top:40px}
.f-col h3{font-size:17px;font-weight:700;padding-bottom:8px;border-bottom:1px solid var(--footer-line);margin-bottom:10px;width:108px}
.links{left:0}
.links ul{list-style:none}
.links li{font-size:13.5px;line-height:27.5px}
.links li::before{content:"› "}
.details{left:175px}
.details h3{width:130px}
.detail{display:flex;gap:10px;font-size:13px;margin-bottom:20px;align-items:flex-start}
.detail svg{flex:none;margin-top:2px}
.detail b{font-weight:700}
.map-col{left:461px}
.map-col h3{width:135px;margin-bottom:12px}
.map{width:268px;height:153px;background:linear-gradient(135deg,#ece8df,#ddd8cc)}
.f-divider{position:absolute;top:50px;width:1px;height:170px;background:rgba(0,0,0,.12)}
.f-brand{position:absolute;right:0;top:112px;display:flex;align-items:center;gap:10px}
.f-brand .brand-mark{background:var(--white)}
.f-brand span{font-size:24px;font-weight:700;color:#dfe8ea}
.bottom-bar{position:absolute;left:0;top:2208px;width:1200px;height:45px;background:var(--bottom);color:var(--white)}
.bottom-bar .wrap{display:flex;justify-content:space-between;align-items:center;height:45px;font-size:11.5px}
.socials{display:flex;gap:9px}
.socials span{width:20px;height:20px;border-radius:50%;border:1.5px solid var(--white);display:block}
</style>
</head>
<body>

<header class="site-header">
  <div class="wrap">
    <div class="brand"><span class="brand-mark"></span><span class="brand-name">SkyNestClips</span></div>
    <div class="contact-line">
      <div class="contact-item"><span class="icon-round"><svg width="17" height="17" viewBox="0 0 24 24"><path fill="#fff" d="M6.6 10.8a15 15 0 0 0 6.6 6.6l2.2-2.2a1 1 0 0 1 1-.25 11.4 11.4 0 0 0 3.6.57 1 1 0 0 1 1 1V20a1 1 0 0 1-1 1A17 17 0 0 1 3 4a1 1 0 0 1 1-1h3.5a1 1 0 0 1 1 1c0 1.25.2 2.450.57 3.57a1 1 0 0 1-.25 1z"/></svg></span>+316 204 88315</div>
      <div class="contact-item email"><span class="icon-round"><svg width="18" height="14" viewBox="0 0 24 18"><path fill="#fff" d="M0 0h24v18H0z"/><path fill="none" stroke="#0b6a6f" stroke-width="2" d="M1 1l11 9 11-9"/></svg></span>contact@skynestclips.example</div>
    </div>
    <nav class="main-nav">
      <a href="#" class="home">HOME</a>
      <a href="#">ABOUT US</a>
      <a href="#" class="active">SERVICES</a>
      <a href="#">PORTFOLIO</a>
      <a href="#">PRICES</a>
      <a href="#">CONTACT US</a>
    </nav>
  </div>
</header>

<section class="hero" role="img" aria-label="Aerial drone hovering above a brick family home surrounded by trees">
  <div class="hero-band">
    <h1>SKYNESTCLIPS</h1>
    <p>We Film Your Home To Increase Your Chances Of Sale</p>
  </div>
</section>

<div class="breadcrumb">
  <div class="wrap">
    <svg width="15" height="13" viewBox="0 0 24 20"><path fill="#222" d="M12 0 0 10h3v10h6v-6h6v6h6V10h3z"/></svg>
    <span class="sep">/</span><span>SERVICES</span>
  </div>
</div>

<h2 class="page-title">SERVICES</h2>

<section class="service first">
  <div class="wrap">
    <div class="service-photo" role="img" aria-label="Pilot holding a remote controller with a white drone in flight" style="background:linear-gradient(135deg,#8a7466,#3a3230 60%,#1e1e22)"></div>
    <div class="service-body">
      <h2>Aerial Video Shooting</h2>
      <p>Lorem Ipsum is simply dummy text of the printing and typesetting industry. Lorem Ipsum has been the industry's standard dummy text ever since the 1500s, when an unknown printer took a galley of type and scrambled it to make a type specimen book. It has survived not only five centuries, but also the leap into electronic typesetting, remaining essentially unchanged.Lorem Ipsum is simply dummy text of the printing and typesetting industry. Lorem Ipsum has been the industry's standard dummy text ever since the 1500s.</p>
      <a href="#" class="read-more">Read More »</a>
    </div>
  </div>
</section>

<section class="service alt">
  <div class="wrap">
    <div class="service-photo" role="img" aria-label="Operator flying a drone in front of a suburban house" style="background:linear-gradient(180deg,#6f9fd6,#a7c3e4 45%,#c9b58e 70%,#4e5a3c)"></div>
    <div class="service-body">
      <h2>Videography</h2>
      <p>Lorem Ipsum is simply dummy text of the printing and typesetting industry. Lorem Ipsum has been the industry's standard dummy text ever since the 1500s, when an unknown printer took a galley of type and scrambled it to make a type specimen book. It has survived not only five centuries, but also the leap into electronic typesetting, remaining essentially unchanged.Lorem Ipsum is simply dummy text of the printing and typesetting industry. Lorem Ipsum has been the industry's standard dummy text ever since the 1500s.</p>
      <a href="#" class="read-more">Read More »</a>
    </div>
  </div>
</section>

<section class="service">
  <div class="wrap">
    <div class="service-photo" role="img" aria-label="Hand launching a drone against a blue sky over a wooden deck" style="background:linear-gradient(160deg,#3d6fb4,#6d8fb3 45%,#5b6a3a 75%,#3b2a22)"></div>
    <div class="service-body">
      <h2>Aerial Real Estate</h2>
      <p>Lorem Ipsum is simply dummy text of the printing and typesetting industry. Lorem Ipsum has been the industry's standard dummy text ever since the 1500s, when an unknown printer took a galley of type and scrambled it to make a type specimen book. It has survived not only five centuries, but also the leap into electronic typesetting, remaining essentially unchanged.Lorem Ipsum is simply dummy text of the printing and typesetting industry. Lorem Ipsum has been the industry's standard dummy text ever since the 1500s.</p>
      <a href="#" class="read-more">Read More »</a>
    </div>
  </div>
</section>

<section class="service alt">
  <div class="wrap">
    <div class="service-photo" role="img" aria-label="Pilot holding a remote controller with a white drone in flight" style="background:linear-gradient(135deg,#8a7466,#3a3230 60%,#1e1e22)"></div>
    <div class="service-body">
      <h2>Aerial Video Shooting</h2>
      <p>Lorem Ipsum is simply dummy text of the printing and typesetting industry. Lorem Ipsum has been the industry's standard dummy text ever since the 1500s, when an unknown printer took a galley of type and scrambled it to make a type specimen book. It has survived not only five centuries, but also the leap into electronic typesetting, remaining essentially unchanged.Lorem Ipsum is simply dummy text of the printing and typesetting industry. Lorem Ipsum has been the industry's standard dummy text ever since the 1500s.</p>
      <a href="#" class="read-more">Read More »</a>
    </div>
  </div>
</section>

<section class="service">
  <div class="wrap">
    <div class="service-photo" role="img" aria-label="Drone flying in front of a large white-columned house with an operator on the driveway" style="background:linear-gradient(180deg,#d8dde4,#9a8574 45%,#6b6a4a 75%,#59523f)"></div>
    <div class="service-body">
      <h2>Videography</h2>
      <p>Lorem Ipsum is simply dummy text of the printing and typesetting industry. Lorem Ipsum has been the industry's standard dummy text ever since the 1500s, when an unknown printer took a galley of type and scrambled it to make a type specimen book. It has survived not only five centuries, but also the leap into electronic typesetting, remaining essentially unchanged.Lorem Ipsum is simply dummy text of the printing and typesetting industry. Lorem Ipsum has been the industry's standard dummy text ever since the 1500s.</p>
      <a href="#" class="read-more">Read More »</a>
    </div>
  </div>
</section>

<footer class="site-footer">
  <div class="wrap">
    <div class="f-col links">
      <h3>Quick Links</h3>
      <ul><li>Home</li><li>About Us</li><li>Services</li><li>Portfolio</li><li>Prices</li><li>Contact Us</li></ul>
    </div>
    <div class="f-divider" style="left:135px"></div>
    <div class="f-col details">
      <h3>Contact Detail</h3>
      <div class="detail"><svg width="12" height="17" viewBox="0 0 12 17"><path fill="#fff" d="M6 0a6 6 0 0 0-6 6c0 4.5 6 11 6 11s6-6.5 6-11a6 6 0 0 0-6-6zm0 8.3A2.3 2.3 0 1 1 6 3.7a2.3 2.3 0 0 1 0 4.6z"/></svg><span><b>SNC,</b> Lorem ipsum dolor sit amet,<br>consectetuer auyipiscing elit</span></div>
      <div class="detail"><svg width="15" height="15" viewBox="0 0 24 24"><path fill="#fff" d="M6.6 10.8a15 15 0 0 0 6.6 6.6l2.2-2.2a1 1 0 0 1 1-.25 11.4 11.4 0 0 0 3.6.57 1 1 0 0 1 1 1V20a1 1 0 0 1-1 1A17 17 0 0 1 3 4a1 1 0 0 1 1-1h3.5a1 1 0 0 1 1 1c0 1.25.2 2.45.57 3.57a1 1 0 0 1-.25 1z"/></svg><b>+316 204 88315</b></div>
      <div class="detail"><svg width="16" height="15" viewBox="0 0 16 15"><path fill="#fff" d="M4 0h8v4H4zM0 5h16v7h-3v3H3v-3H0zm5 5v3h6v-3z"/></svg><b>+316 204 88315</b></div>
      <div class="detail"><svg width="16" height="12" viewBox="0 0 24 18"><path fill="#fff" d="M0 0h24v18H0z"/><path fill="none" stroke="#0b6a6f" stroke-width="2" d="M1 1l11 9 11-9"/></svg><b>contact@skynestclips.example</b></div>
    </div>
    <div class="f-divider" style="left:428px"></div>
    <div class="f-col map-col">
      <h3>Map</h3>
      <div class="map" role="img" aria-label="Street map showing the office location"></div>
    </div>
    <div class="f-divider" style="left:760px"></div>
    <div class="f-brand"><span class="brand-mark"></span><span>SkyNestClips</span></div>
  </div>
</footer>

<div class="bottom-bar">
  <div class="wrap">
    <span>Copyright © 2016 SkyNestClips.&nbsp; All Rights Reserved</span>
    <div class="socials"><span></span><span></span><span></span></div>
  </div>
</div>

</body>
</html>
```